Conservative, Modern and Sharp Builder Business card

Hi there,
We would like to update our existing business card.
I have attached photos of existing business card, logo and van sign.

I would like the business card to also list what we do :
Renovation • New Build • Alteration
Extension • Bathroom • Maintenance.(Seperated by dots)

Contact number : 021 0483 0752
(With that exact spacing)

Ideally when people looking from about 2-3 metres, they know that it is a builder’s business card

Open to suggestions on fonts, layout, style of business card

PLEASE ONLY SUBMIT YOUR BEST OR MAX 3 DESIGNS FOR EACH DESIGNER

Thanks

Industry/Entity Type

Construction. Renovation

Contact Information for Business Card

Details should be the same as the existing card. And addition of what we do.

Requirements
Should not have
• The new business card must not have the same layout as our existing one. Thanks

```html
<!DOCTYPE html>
<html lang="en">
<head>
<meta charset="utf-8">
<title>FrameLine Business Card</title>
<link href="https://fonts.googleapis.com/css2?family=Roboto:wght@400;700&display=swap" rel="stylesheet">
<style>
  :root {
    --backdrop: #5b3f2c;
    --card-light: #e6e6e6;
    --card-dark: #231f20;
    --ink: #3a3a3a;
    --ink-soft: #444;
    --band-dark: #231f20;
    --band-grey: #404040;
    --ghost: #3f3d3e;
    --ghost-text: #4c4a4b;
  }
  * { margin: 0; padding: 0; box-sizing: border-box; }
  html, body { width: 1200px; height: 960px; overflow: hidden; }
  body {
    background: var(--backdrop);
    font-family: "Roboto", Arial, sans-serif;
    position: relative;
  }
  .card {
    position: absolute;
    left: 281px;
    width: 637px;
    box-shadow: 0 4px 14px rgba(0,0,0,.35);
  }
  .card-front { top: 95px; height: 364px; background: var(--card-light); }
  .card-back { top: 511px; height: 361px; background: var(--card-dark); }

  .brand-block {
    position: absolute; left: 150px; top: 268px; width: 130px;
    text-align: center; color: var(--ink);
  }
  .card-front .brand-block { top: 162px; left: 140px; width: 150px; }
  .brand-name {
    display: flex; align-items: center; justify-content: center; gap: 6px;
    font-weight: 700; font-size: 21px; letter-spacing: .2px;
  }
  .brand-square { width: 9px; height: 9px; background: currentColor; }
  .brand-services {
    margin-top: 12px; font-size: 7.4px; line-height: 9.4px; color: #222;
    white-space: nowrap;
  }

  .divider {
    position: absolute; left: 312px; top: 122px; width: 3px; height: 128px;
    background: var(--ink-soft);
  }
  .person { position: absolute; left: 350px; top: 112px; color: var(--ink); }
  .person-name { font-size: 25px; line-height: 30px; }
  .person-role { font-size: 14.5px; line-height: 16px; }

  .contacts {
    position: absolute; left: 350px; top: 181px; list-style: none;
    color: var(--ink); font-size: 15px;
  }
  .contacts li { display: flex; align-items: center; height: 18.3px; }
  .contacts svg { width: 12px; height: 12px; margin-right: 10px; fill: var(--ink); }

  .band { position: absolute; bottom: 0; height: 17px; }
  .band-left { left: 0; width: 313px; background: var(--band-dark); }
  .band-right { left: 316px; right: 0; background: var(--band-grey); }

  .back-name {
    position: absolute; left: 0; right: 0; top: 148px; text-align: center;
    font-weight: 700; font-size: 44px; color: var(--ghost);
    display: flex; justify-content: center; align-items: center; gap: 12px;
  }
  .back-name .brand-square { width: 16px; height: 16px; }
  .back-rule {
    position: absolute; left: 83px; width: 473px; top: 209px; height: 2px;
    background: var(--ghost);
  }
  .back-services {
    position: absolute; left: 0; right: 0; top: 238px; text-align: center;
    font-size: 19.5px; line-height: 25px; color: var(--ghost-text);
  }
</style>
</head>
<body>
  <section class="card card-front">
    <div class="brand-block">
      <div class="brand-name"><span class="brand-square"></span>FrameLine</div>
      <p class="brand-services">Renovation • New Build • Alteration<br>Extension • Bathroom • Maintenance.</p>
    </div>
    <div class="divider"></div>
    <div class="person">
      <h1 class="person-name" style="font-weight:400">Daniel Harper</h1>
      <p class="person-role">Residential Builder</p>
    </div>
    <ul class="contacts">
      <li><svg viewBox="0 0 24 24"><path d="M6.6 10.8a15 15 0 0 0 6.6 6.6l2.2-2.2c.3-.3.7-.4 1-.2 1.1.4 2.3.6 3.6.6.6 0 1 .4 1 1V20c0 .6-.4 1-1 1A17 17 0 0 1 3 4c0-.6.4-1 1-1h3.5c.6 0 1 .4 1 1 0 1.3.2 2.5.6 3.6.1.3 0 .7-.2 1z"/></svg>021 0483 0752</li>
      <li><svg viewBox="0 0 24 24"><path d="M2 5h20v14H2z M2 5l10 8 10-8" stroke="#e6e6e6" stroke-width="1.5"/></svg>hello@frameline.nz</li>
      <li><svg viewBox="0 0 24 24"><circle cx="12" cy="12" r="10"/><path d="M2 12h20M12 2c3 3 3 17 0 20M12 2c-3 3-3 17 0 20" stroke="#e6e6e6" stroke-width="1.5" fill="none"/></svg>www.FrameLine.nz</li>
      <li><svg viewBox="0 0 24 24"><circle cx="12" cy="12" r="9" fill="none" stroke="#3a3a3a" stroke-width="2.5"/></svg>FrameLine.nz</li>
    </ul>
    <div class="band band-left"></div>
    <div class="band band-right"></div>
  </section>

  <section class="card card-back">
    <div class="back-name"><span class="brand-square"></span>FrameLine</div>
    <div class="back-rule"></div>
    <p class="back-services">Renovation • New Build • Alteration<br>Extension • Bathroom • Maintenance.</p>
  </section>
</body>
</html>
```